Need a FLAT UI design for mobile campus Marketplace APP

We need to improve our current UI/UX design for a mobile application called Tradlo. It is designed for students to buy and sell their goods, such as books and furnitures, on their own campus to save living expenses. Our initial design does not look very flat and clear enough. We would like to see a flat design improvement for a better purchasing and selling experience using yellow as theme color.

Target Market(s)

college students

Industry/Entity Type

Marketplace

Colors
ffc214
ffcf3e
fee18a
fff3d1

Requirements
Must have
• an improved UI look, flat and simple.
Nice to have
• alternative designs
Should not have
• a new function design for the app on the design

```html
<!DOCTYPE html>
<html lang="en">
<head>
<meta charset="utf-8">
<title>Tradlo – App Design</title>
<link rel="stylesheet" href="https://fonts.googleapis.com/css2?family=Open+Sans:wght@400;600;700&display=swap">
<style>
:root{
  --yellow:#ffc214;
  --yellow-mid:#ffcf3e;
  --yellow-soft:#fee18a;
  --yellow-pale:#fff3d1;
  --ink:#1d1d1d;
  --ink-soft:#4a4a4a;
  --white:#ffffff;
  --bubble-grey:#e9e9ec;
  --page:#f4f1ea;
}
*{box-sizing:border-box;margin:0;padding:0}
html,body{width:1070px;height:1200px;overflow:hidden}
body{background:var(--page);font-family:"Open Sans",Arial,sans-serif;color:var(--ink);position:relative}

.header{position:absolute;left:60px;top:90px;display:flex;align-items:center;gap:34px}
.app-tile{width:130px;height:130px;border-radius:10px;background:var(--yellow);display:flex;align-items:center;justify-content:center}
.app-tile .brand{color:var(--white);font-weight:700;font-size:26px}
.header-title{font-size:32px;font-weight:400;color:var(--ink)}

.screens{position:absolute;left:30px;top:320px;display:flex;gap:40px}
.screen{width:310px;height:550px;position:relative;overflow:hidden;background:var(--white);box-shadow:0 6px 24px rgba(0,0,0,.12)}

/* splash */
.splash-photo{position:absolute;inset:0;background:linear-gradient(160deg,#8a6a55 0%,#5d4a40 35%,#3f4a48 70%,#2a3836 100%)}
.splash-content{position:absolute;left:0;right:0;top:175px;text-align:center;color:var(--white)}
.splash-tile{width:88px;height:88px;margin:0 auto 22px;border-radius:6px;background:var(--yellow);display:flex;align-items:center;justify-content:center}
.splash-tile .brand{color:var(--white);font-weight:700;font-size:17px}
.splash-tagline{font-size:17px;line-height:25px;text-shadow:0 1px 3px rgba(0,0,0,.4)}

/* status bar */
.status-bar{height:20px;display:flex;align-items:center;justify-content:space-between;padding:0 10px;font-size:9px}
.status-bar .battery{display:inline-block;width:18px;height:8px;border:1px solid currentColor;vertical-align:middle;margin-left:3px;position:relative}
.status-bar .battery::after{content:"";position:absolute;left:1px;top:1px;bottom:1px;width:11px;background:currentColor}

/* edit information */
.edit-bg{position:absolute;inset:0;background:linear-gradient(170deg,#2b2a28 0%,#5a4f43 30%,#8c7f6f 55%,#6b6358 75%,#3c3a36 100%)}
.edit{position:relative;color:var(--white);height:100%}
.edit .status-bar{background:rgba(0,0,0,.35)}
.edit-nav{height:50px;display:flex;align-items:center;padding-left:14px;gap:28px}
.edit-nav h1{font-size:21px;font-weight:600}
.profile-row{display:flex;justify-content:space-between;align-items:center;padding:12px 40px 0 42px}
.profile-email{font-size:10px}
.profile-state{font-size:7px;opacity:.85;margin-top:3px;display:flex;align-items:center;gap:4px}
.profile-state::before{content:"";width:5px;height:5px;border-radius:50%;background:#35c46b}
.avatar{width:70px;height:68px;border:2px solid var(--yellow);border-radius:4px;background:linear-gradient(135deg,#d7b48c,#a6805f 60%,#6e5845)}
.fields{margin:14px 40px 0 42px;display:flex;flex-direction:column;gap:7px}
.field{height:32px;background:rgba(255,255,255,.18);display:flex;align-items:center;gap:14px;padding-left:12px;font-size:11px;color:rgba(255,255,255,.65)}
.save-btn{margin:8px 40px 0 42px;height:34px;background:var(--yellow);color:var(--ink);font-size:12px;display:flex;align-items:center;justify-content:center}
.filters{margin:18px 40px 0 42px;display:flex;gap:4px}
.filter{flex:1;height:74px;background:rgba(255,255,255,.2);display:flex;flex-direction:column;align-items:center;justify-content:center;gap:8px;font-size:10.5px}
.resend{position:absolute;left:0;right:0;bottom:0;height:34px;background:var(--yellow);color:var(--ink);font-size:11px;display:flex;align-items:center;justify-content:center}

/* chat */
.chat-bg{position:absolute;inset:0;background:linear-gradient(170deg,#b9b3aa 0%,#8d8a85 40%,#c8c2b6 70%,#9c978f 100%)}
.chat{position:relative;height:100%}
.chat-top{background:var(--yellow);color:var(--ink)}
.chat-nav{height:24px;display:flex;align-items:center;justify-content:space-between;padding:0 8px;font-size:11px}
.chat-nav .back{display:flex;align-items:center;gap:6px}
.messages{padding:10px 10px 0;display:flex;flex-direction:column;font-size:11px;line-height:13px}
.bubble{padding:4px 9px;border-radius:8px;max-width:78%}
.bubble.out{align-self:flex-end;background:var(--yellow)}
.bubble.in{align-self:flex-start;background:var(--bubble-grey)}
.stamp{align-self:center;font-size:7px;color:var(--yellow);margin:3px 0 0}
.composer{position:absolute;left:0;right:0;bottom:46px;height:30px;background:var(--white);padding:5px 8px}
.composer-field{height:18px;border:1px solid #d8d8d8;font-size:9px;color:#aaa;padding:2px 5px}
.tab-bar{position:absolute;left:0;right:0;bottom:0;height:46px;background:var(--yellow);display:flex}
.tab{flex:1;display:flex;flex-direction:column;align-items:center;justify-content:center;gap:3px;font-size:8px;color:var(--ink)}
.tab.active{background:var(--white)}
</style>
</head>
<body>

<header class="header">
  <div class="app-tile"><span class="brand">Tradlo</span></div>
  <h2 class="header-title">App Design</h2>
</header>

<main class="screens">

  <!-- Splash -->
  <section class="screen splash">
    <div class="splash-photo" role="img" aria-label="Photo of a smiling group of students posing together"></div>
    <div class="splash-content">
      <div class="splash-tile"><span class="brand">Tradlo</span></div>
      <p class="splash-tagline">Buy or Sell,<br>in a better &amp; Reliable Way</p>
    </div>
  </section>

  <!-- Edit information -->
  <section class="screen">
    <div class="edit-bg" role="img" aria-label="Blurred campus background photo"></div>
    <div class="edit">
      <div class="status-bar"><span>••• Novacell</span><span>1:43 pm</span><span>80%<i class="battery"></i></span></div>
      <div class="edit-nav">
        <svg width="14" height="22" viewBox="0 0 14 22"><path d="M12 2 3 11l9 9" fill="none" stroke="#ffc214" stroke-width="3"/></svg>
        <h1>Edit Information</h1>
      </div>
      <div class="profile-row">
        <div>
          <div class="profile-email">lena.hart@tradlo.com</div>
          <div class="profile-state">Not Activated</div>
        </div>
        <div class="avatar" role="img" aria-label="Profile photo of the user"></div>
      </div>
      <div class="fields">
        <div class="field">
          <svg width="10" height="11" viewBox="0 0 10 11"><circle cx="5" cy="3" r="2.5" fill="#ddd"/><path d="M0 11c0-3 2-5 5-5s5 2 5 5z" fill="#ddd"/></svg>Alex</div>
        <div class="field">
          <svg width="10" height="10" viewBox="0 0 10 10"><rect x="0" y="3" width="10" height="7" fill="#ddd"/><rect x="3" y="0" width="4" height="3" fill="none" stroke="#ddd"/></svg>Main Library</div>
        <div class="field">
          <svg width="9" height="11" viewBox="0 0 9 11"><rect x=".5" y=".5" width="8" height="10" fill="none" stroke="#ddd"/><path d="M2 4h5M2 6h5M2 8h3" stroke="#ddd"/></svg>City / State</div>
      </div>
      <div class="save-btn">SAVE</div>
      <div class="filters">
        <div class="filter">
          <svg width="22" height="22" viewBox="0 0 22 22"><rect x="1" y="1" width="20" height="20" fill="none" stroke="#fff" stroke-width="1.5"/><rect x="5" y="5" width="5" height="5" fill="#fff"/><rect x="12" y="5" width="5" height="5" fill="#fff"/><rect x="5" y="12" width="5" height="5" fill="#fff"/><rect x="12" y="12" width="5" height="5" fill="#fff"/></svg>
          By Catagory</div>
        <div class="filter">
          <svg width="20" height="24" viewBox="0 0 20 24"><circle cx="10" cy="6" r="5" fill="none" stroke="#fff" stroke-width="1.5"/><path d="M1 23c0-6 4-10 9-10s9 4 9 10z" fill="none" stroke="#fff" stroke-width="1.5"/></svg>
          By Seller/ Buyer</div>
      </div>
      <div class="resend">Resend Activation Email</div>
    </div>
  </section>

  <!-- Chat -->
  <section class="screen">
    <div class="chat-bg" role="img" aria-label="Blurred background photo behind the conversation"></div>
    <div class="chat">
      <div class="chat-top">
        <div class="status-bar"><span>••• Novacell</span><span>1:43 pm</span><span>80%<i class="battery"></i></span></div>
        <div class="chat-nav">
          <span class="back"><svg width="8" height="12" viewBox="0 0 8 12"><path d="M7 1 2 6l5 5" fill="none" stroke="#1d1d1d" stroke-width="1.6"/></svg>Chat</span>
          <span>Mark Daniel Ross</span>
          <span>Profile</span>
        </div>
      </div>
      <div class="messages">
        <div class="bubble out">How are you?</div>
        <div class="bubble in" style="margin-top:10px">My Friend</div>
        <div class="bubble out" style="margin-top:6px">?????</div>
        <div class="bubble in" style="margin-top:22px;max-width:72%">Just chillin' and buildin'. Assets for the PSDs are almost done. Just have about a dozen items left.</div>
        <div class="stamp">Thu, Sep 19, 1:26 PM</div>
        <div class="bubble out" style="margin-top:44px;max-width:74%">We wish create a CRM Portal on the Corebase portal, we have someone to do the actual coding and design so just need the User Interface designing</div>
      </div>
      <div class="composer"><div class="composer-field">Message</div></div>
      <nav class="tab-bar">
        <div class="tab"><svg width="14" height="13" viewBox="0 0 14 13"><path d="M1 5.5C1 3 3.7 1 7 1s6 2 6 4.5S10.3 10 7 10H5l-3 2 .7-3C1.6 8 1 6.8 1 5.5z" fill="none" stroke="#1d1d1d"/></svg>Chat</div>
        <div class="tab"><svg width="14" height="13" viewBox="0 0 14 13"><path d="M1 4h11M9 1l3 3-3 3M13 9H2M5 6 2 9l3 3" fill="none" stroke="#1d1d1d"/></svg>Trade</div>
        <div class="tab active"><svg width="15" height="13" viewBox="0 0 15 13"><path d="M7.5 0 0 6.5h2V13h4V9h3v4h4V6.5h2z" fill="#1d1d1d"/></svg>HOME</div>
        <div class="tab"><svg width="13" height="13" viewBox="0 0 13 13"><rect x=".5" y="2.5" width="10" height="10" fill="none" stroke="#1d1d1d"/><path d="M5 8l7-7" stroke="#1d1d1d" stroke-width="1.4"/></svg>Post</div>
        <div class="tab"><svg width="11" height="13" viewBox="0 0 11 13"><circle cx="5.5" cy="3.5" r="3" fill="#1d1d1d"/><path d="M0 13c0-4 2.5-6 5.5-6s5.5 2 5.5 6z" fill="#1d1d1d"/></svg>Account</div>
      </nav>
    </div>
  </section>

</main>
</body>
</html>
```